依頼詳細
当会議が主催する講演会のチラシ製作をお願いいたします。
載せていただきたい事項は記載項目のとおりです。

【デザイン等について】
・昨年のチラシを添付しますので、参考にしてください。
・デザイン、レイアウト、色合いなどは全てお任せします
・昨年のデザインは堅苦しい印象がありましたので、今年はもう少し自由度のあるデザインを希望いたします。
・PRの強化に繋がるような、分かりやすく、且つ講演会に行きたくなる、目を引くようなデザインにしていただけたら幸いです。
・講師の写真を1枚載せてください(添付の写真データを使用願います)
・A4 縦 フルカラー
記載項目
キャッチコピー:地方の実情に合った新幹線の在り方について学ぼう

講演:「白峰新幹線実現の可能性を探る~在来線、ミニ新幹線からフル規格の新幹線へ~」

講師:鉄道ジャーナリスト 柴田 亮 氏

とき:平成28年7月5日(火) 午後3時~

ところ:桐ヶ丘グランドホテル
桐ヶ丘市松葉町二丁目3番4号

主催:北辰新幹線青葉延伸推進会議

お問い合わせ:北辰新幹線青葉延伸推進会議事務局(桐ヶ丘市役所企画課内)
Tel 0199-42-8670

※「申込不要・入場無料」の文言を入れてください。
サイズ
A4
ページ数
片面
希望イメージ
シンプル 複雑
単色 カラフル
暗い 明るい
日常 高級
遊び心 厳粛
未来的 伝統的
女性的 男性的
希望する色
納品ファイル
• イラストレーター形式 (.ai)
補足説明
※イラストレーターファイルはアウトライン必須、カラーモードはCMYKで納品願います。
※PDF形式も納品願います。
※納品は電子メール形式でお願いします。
※提案いただいたデザインの中から必ずコンペの当選者を選定します。(内容によっては修正をお願いする場合があります)
※ 募集期間を6月15日(水)としておりましたが、提案件数が希望数に達したため、誠に勝手ながら、6月14日(火)の正午をもって締め切りとさせていただく予定ですのでご了承ください。

明るく、非常に分かりやすいデザインであり、やわらかくかつポップなデザインが気に入りました。

この度は素敵なデザインを提案していただき誠にありがとうございました。
クラウドソーシングのサービスを今回初めて利用させていただきましたが、スピーディーでかつ素晴らしいデザインを提案いただき正直驚きました。想像していた以上のデザインで非常にうれしく思っております。今後ともどうか一つよろしくお願いいたします。

```html
<!DOCTYPE html>
<html lang="ja">
<head>
<meta charset="utf-8">
<title>講演会のご案内</title>
<link href="https://fonts.googleapis.com/css2?family=Noto+Sans+JP:wght@500;700;900&display=swap" rel="stylesheet">
<style>
  :root {
    --navy: #17285c;
    --blue: #1f63b8;
    --sky: #7fb8e6;
    --band: #a9d2f0;
    --bg-top: #d9e6f2;
    --bg-bottom: #f2f6fa;
    --red: #e0241b;
    --orange: #e86a12;
    --white: #ffffff;
  }
  * { margin: 0; padding: 0; box-sizing: border-box; }
  html, body { width: 849px; height: 1200px; overflow: hidden; }
  body { font-family: "Noto Sans JP", sans-serif; color: var(--navy); }
  .flyer {
    position: relative; width: 849px; height: 1200px; overflow: hidden;
    background: linear-gradient(180deg, var(--bg-top) 0%, var(--bg-bottom) 60%, #e4edf6 100%);
  }
  .headline { position: absolute; left: 58px; top: 22px; font-weight: 900; line-height: 1; }
  .headline__lead, .headline__tail { font-size: 58px; color: var(--navy); letter-spacing: 1px; }
  .headline__main {
    font-size: 96px; margin: 14px 0 16px -6px; letter-spacing: 1px;
    background: linear-gradient(180deg, #3b8ee0, #164f9e);
    -webkit-background-clip: text; background-clip: text; -webkit-text-fill-color: transparent;
  }
  .entry-badge {
    position: absolute; right: 30px; top: 180px; width: 132px; padding: 10px 0;
    background: var(--white); border-radius: 10px; text-align: center;
    font-weight: 900; font-size: 23px; line-height: 1.35; color: var(--navy);
  }
  .train-visual {
    position: absolute; left: 0; top: 262px; width: 849px; height: 428px;
    background: linear-gradient(160deg, rgba(255,255,255,0) 0%, #c9c6d9 30%, #9c8fb8 55%, #5c5a78 75%, rgba(217,230,242,0) 100%);
  }
  .lecture-tag, .info-tag {
    position: absolute; left: 28px; background: var(--navy); color: var(--white);
    font-weight: 900; text-align: center;
  }
  .lecture-tag { top: 686px; width: 112px; height: 42px; font-size: 28px; line-height: 42px; border-radius: 6px 6px 0 0; }
  .lecture-band {
    position: absolute; left: 0; top: 728px; width: 849px; height: 92px;
    background: linear-gradient(180deg, var(--band), var(--sky)); text-align: center;
  }
  .lecture-band__title { font-size: 47px; font-weight: 900; line-height: 1; margin-top: 8px; letter-spacing: 1px; }
  .lecture-band__sub { font-size: 22px; font-weight: 700; margin-top: 8px; }
  .speaker-credit {
    position: absolute; left: 620px; top: 826px; font-size: 18px; font-weight: 700; line-height: 1.3;
  }
  .speaker-credit strong { font-size: 24px; font-weight: 900; margin-left: 20px; }
  .info-tag { width: 100px; height: 58px; font-size: 30px; line-height: 58px; border-radius: 6px; }
  .info-tag--date { top: 850px; }
  .info-tag--venue { top: 948px; }
  .date {
    position: absolute; left: 150px; top: 832px; font-weight: 900; color: var(--blue);
    font-size: 40px; display: flex; align-items: baseline; gap: 4px; line-height: 1;
  }
  .date__num { font-size: 76px; color: var(--red); }
  .date__day {
    display: inline-block; width: 40px; height: 40px; border-radius: 50%; background: var(--navy);
    color: var(--white); font-size: 22px; text-align: center; line-height: 40px; margin-left: 6px;
  }
  .date-time {
    position: absolute; left: 250px; top: 908px; font-size: 28px; font-weight: 900;
    color: var(--red); line-height: 1; white-space: nowrap;
  }
  .venue { position: absolute; left: 150px; top: 948px; }
  .venue__name { font-size: 38px; font-weight: 900; color: var(--orange); line-height: 58px; white-space: nowrap; }
  .venue__address { font-size: 20px; font-weight: 700; margin-top: 2px; }
  .speaker-photo {
    position: absolute; left: 620px; top: 888px; width: 200px; height: 200px;
    background: linear-gradient(180deg, #e7eef5 0%, #cfd8e2 60%, #3d4656 100%);
  }
  .organizer { position: absolute; left: 30px; top: 1090px; font-size: 19px; font-weight: 700; line-height: 1.4; }
</style>
</head>
<body>
<main class="flyer">
  <h1 class="headline">
    <div class="headline__lead">地方の実情に合った</div>
    <div class="headline__main">新幹線の在り方</div>
    <div class="headline__tail">について学ぼう</div>
  </h1>
  <div class="entry-badge">申込不要<br>入場無料</div>

  <div class="train-visual" role="img" aria-label="銀色と紫の新幹線車両が走る写真"></div>

  <div class="lecture-tag">講演</div>
  <section class="lecture-band">
    <h2 class="lecture-band__title">白峰新幹線実現の可能性を探る</h2>
    <p class="lecture-band__sub">～在来線、ミニ新幹線からフル規格の新幹線へ～</p>
  </section>
  <p class="speaker-credit">講師：鉄道ジャーナリスト<br><strong>柴田 亮</strong> 氏</p>

  <div class="info-tag info-tag--date">日時</div>
  <div class="date">
    <span class="date__num">7</span>月<span class="date__num">5</span>日<span class="date__day">火</span>
  </div>
  <div class="date-time">PM15:00～</div>

  <div class="info-tag info-tag--venue">会場</div>
  <div class="venue">
    <div class="venue__name">桐ヶ丘グランドホテル</div>
    <div class="venue__address">桐ヶ丘市松葉町二丁目3番4号</div>
  </div>

  <div class="speaker-photo" role="img" aria-label="講師 柴田 亮 氏の写真"></div>

  <footer class="organizer">
    主催：北辰新幹線青葉延伸推進会議<br>
    お問い合わせ<br>
    北辰新幹線青葉延伸推進会議事務局<br>
    （桐ヶ丘市役所企画課内）　Tel　0199-42-8670
  </footer>
</main>
</body>
</html>
```